Business Card Design

We need a business card design for a new company based in Melbourne Australia. We are financial broker in finance industry. We provide a wide range of finance solutions to our clients including home loans, commercial loans, business facilities, car loans, equipment loans, invoice finance, etc. The company name is from director's personal name. We would like to have a new company logo that includes KT.

Industry/Entity Type

Business

Contact Information for Business Card

company name: KT & Co Finance Pty Ltd
person's name: Kenneth Tollard
role: Managing Director
Mobile: 0417 638 294
fax: 03 9561 2047
Email: kenneth.tollard@ktcofinance.example
Address: Suite 4/718 Marlow Avenue Ferndale East Vic 3187
Credit Licence No.: 382917

```html
<!DOCTYPE html>
<html lang="en">
<head>
<meta charset="utf-8">
<title>KT &amp; Co Finance – Business Card</title>
<link rel="stylesheet" href="https://fonts.googleapis.com/css2?family=Syncopate:wght@700&family=Marcellus+SC&family=Josefin+Sans:wght@400;600&display=swap">
<style>
  :root {
    --brand-red: #f21414;
    --ink-red: #e8101a;
    --paper: #ffffff;
    --icon-red: #e8231c;
    --icon-violet: #6a3df0;
    --tone-lime: #b8e61c;
    --tone-green: #3ed62a;
    --tone-red: #e51a1a;
    --tone-yellow: #f7dc12;
    --tone-blue: #1e7fe6;
    --tone-cyan: #35c9ef;
    --tone-orange: #f2821a;
  }
  * { margin: 0; padding: 0; box-sizing: border-box; }
  html, body { width: 1200px; height: 741px; overflow: hidden; background: var(--paper); }
  .card { position: relative; width: 1200px; height: 741px; background: var(--paper); overflow: hidden; }

  .pattern-band { position: absolute; inset: 0; width: 1200px; height: 741px; }

  .holder-name {
    position: absolute; left: 414px; top: 52px;
    font-family: "Syncopate", "Arial Black", sans-serif; font-weight: 700;
    font-size: 44px; letter-spacing: 1px; color: var(--ink-red); white-space: nowrap;
  }
  .holder-role {
    position: absolute; left: 416px; top: 104px;
    font-family: "Marcellus SC", "Times New Roman", serif;
    font-size: 36px; letter-spacing: 3px; color: var(--ink-red);
  }

  .contact-list { position: absolute; left: 566px; top: 162px; list-style: none; }
  .contact-item {
    display: flex; align-items: center; gap: 14px;
    font-family: "Josefin Sans", "Helvetica", sans-serif; font-size: 18px;
    color: var(--ink-red); letter-spacing: 0.6px;
  }
  .contact-item + .contact-item { margin-top: 16px; }
  .contact-icon { width: 38px; height: 38px; flex: none; }
  .phone-lines { line-height: 1.35; margin-left: 8px; }
  .licence {
    position: absolute; left: 652px; top: 316px;
    font-family: "Josefin Sans", "Helvetica", sans-serif; font-size: 18px;
    color: var(--ink-red); letter-spacing: 0.6px;
  }

  .brand-mark { position: absolute; left: 198px; top: 372px; display: flex; align-items: center; gap: 16px; }
  .brand-dot { width: 120px; height: 120px; border-radius: 50%; background: var(--brand-red); }
  .brand-initials {
    font-family: "Syncopate", "Arial Black", sans-serif; font-weight: 700;
    font-size: 52px; color: var(--brand-red);
  }

  .company-name {
    position: absolute; left: 103px; top: 580px; width: 400px; text-align: center;
    font-family: "Syncopate", "Arial Black", sans-serif; font-weight: 700;
    font-size: 23px; line-height: 1.35; letter-spacing: 1px; color: var(--ink-red);
    text-transform: uppercase;
  }
</style>
</head>
<body>
<main class="card">
  <svg class="pattern-band" viewBox="0 0 1200 741" role="img" aria-label="Multicoloured geometric triangle mosaic forming a zigzag band across the card">
    <defs>
      <linearGradient id="band-upper" x1="0" y1="0" x2="1" y2="1">
        <stop offset="0" stop-color="var(--tone-lime)"/>
        <stop offset="0.3" stop-color="var(--tone-green)"/>
        <stop offset="0.55" stop-color="var(--tone-red)"/>
        <stop offset="0.8" stop-color="var(--tone-yellow)"/>
        <stop offset="1" stop-color="var(--tone-blue)"/>
      </linearGradient>
      <linearGradient id="band-lower" x1="0" y1="0" x2="1" y2="0">
        <stop offset="0" stop-color="var(--tone-cyan)"/>
        <stop offset="0.35" stop-color="var(--tone-blue)"/>
        <stop offset="0.6" stop-color="var(--tone-red)"/>
        <stop offset="0.8" stop-color="var(--tone-yellow)"/>
        <stop offset="1" stop-color="var(--tone-green)"/>
      </linearGradient>
      <linearGradient id="band-left" x1="0" y1="0" x2="1" y2="1">
        <stop offset="0" stop-color="var(--tone-red)"/>
        <stop offset="0.5" stop-color="var(--tone-orange)"/>
        <stop offset="1" stop-color="var(--tone-cyan)"/>
      </linearGradient>
    </defs>
    <polygon fill="url(#band-upper)" points="71,44 300,44 700,444 643,616 289,267"/>
    <polygon fill="url(#band-left)" points="71,180 180,180 289,267 71,480"/>
    <polygon fill="url(#band-lower)" points="643,616 700,444 872,616 1139,349 1139,698 643,698"/>
  </svg>

  <h1 class="holder-name">KENNETH TOLLARD</h1>
  <p class="holder-role">Managing Director</p>

  <ul class="contact-list">
    <li class="contact-item">
      <svg class="contact-icon" viewBox="0 0 38 38" aria-hidden="true">
        <circle cx="19" cy="19" r="18" fill="var(--icon-red)"/>
        <path d="M19 9a7 7 0 0 0-7 7c0 5 7 12 7 12s7-7 7-12a7 7 0 0 0-7-7z" fill="none" stroke="#fff" stroke-width="1.8"/>
        <circle cx="19" cy="16" r="2.5" fill="none" stroke="#fff" stroke-width="1.6"/>
      </svg>
      <span>Suite 4/718 Marlow Avenue Ferndale East Vic 3187</span>
    </li>
    <li class="contact-item">
      <svg class="contact-icon" viewBox="0 0 38 38" aria-hidden="true">
        <circle cx="19" cy="19" r="18" fill="var(--icon-red)"/>
        <rect x="10" y="13" width="18" height="13" fill="none" stroke="#fff" stroke-width="1.8"/>
        <path d="M10 13l9 7 9-7" fill="none" stroke="#fff" stroke-width="1.8"/>
      </svg>
      <span>kenneth.tollard@ktcofinance.example</span>
    </li>
    <li class="contact-item">
      <svg class="contact-icon" viewBox="0 0 38 38" aria-hidden="true">
        <circle cx="19" cy="19" r="18" fill="var(--icon-violet)"/>
        <path d="M13 10c1-1 2-1 3 0l2 3c.6 1 .3 2-.5 2.6l-1 .8c1 2.4 3 4.4 5.3 5.4l.8-1c.6-.8 1.6-1.1 2.6-.5l3 2c1 .7 1 2 0 3l-1.5 1.5c-1.5 1.5-5 .5-8.7-3.2S10 14 11.5 12.5z" fill="#fff"/>
      </svg>
      <span class="phone-lines">0417 638 294<br>(fax)03 9561 2047</span>
    </li>
  </ul>
  <p class="licence">Credit Licence No.: 382917</p>

  <div class="brand-mark">
    <span class="brand-dot" aria-hidden="true"></span>
    <span class="brand-initials">KT</span>
  </div>

  <p class="company-name">KT &amp; Co<br>Finance Pty Ltd</p>
</main>
</body>
</html>
```